Remodel Flyer for realtors

"K" Tandem Builders

4"x 9" rack card front and back

www.BrindleyRenovator.com

555-318-4762

Let us fix what your home inspector finds!

Send us your inspection summary.

We are a licensed and Insured contractor.
CRC4871093

Serving
Marion County and The Heronfield

This flyer will sit in realtor offices for realtors to give to there buyers and sellers.

Target Market(s)

Realtors

Industry/Entity Type

Construction

Colors

Designer to choose colors to be used in the design.

```html
<!DOCTYPE html>
<html lang="en">
<head>
<meta charset="utf-8">
<title>"K" Tandem Builders – Rack Card</title>
<link rel="stylesheet" href="https://fonts.googleapis.com/css2?family=Anton&family=Montserrat:wght@700;800&family=Roboto:wght@400&display=swap">
<style>
  :root {
    --orange: #f39200;
    --orange-deep: #e47f00;
    --navy: #262c36;
    --ink-grey: #555659;
    --ink-navy: #1f2633;
    --white: #ffffff;
    --frame: #3a3f47;
  }
  html, body {
    margin: 0;
    padding: 0;
    overflow: hidden;
  }
  body {
    width: 1200px;
    height: 2683px;
    position: relative;
    background: #e9edf1;
  }
  .rack-card {
    position: absolute;
    inset: 0;
    width: 1200px;
    height: 2683px;
    overflow: hidden;
  }
  .interior-photo {
    position: absolute;
    left: 0;
    top: 300px;
    width: 1200px;
    height: 2200px;
    background:
      linear-gradient(180deg, #f4f6f8 0%, #e6eaee 30%, #dfe4ea 55%, #aab4c2 75%, #6f7d93 100%);
  }
  .wave-layer {
    position: absolute;
    inset: 0;
    width: 1200px;
    height: 2683px;
  }
  .brand {
    position: absolute;
    left: 640px;
    top: 116px;
    width: 520px;
    text-align: center;
    color: var(--white);
    font-family: "Montserrat", sans-serif;
    font-weight: 800;
  }
  .brand-mark {
    width: 150px;
    height: 150px;
    margin: 0 auto 40px;
    background: var(--orange);
  }
  .brand-name {
    font-size: 58px;
    line-height: 1;
    letter-spacing: 2px;
  }
  .brand-sub {
    font-size: 30px;
    line-height: 1;
    letter-spacing: 22px;
    margin-top: 16px;
    padding-left: 22px;
  }
  .info-panel {
    position: absolute;
    left: 50px;
    top: 765px;
    width: 1079px;
    height: 1076px;
    border: 5px solid var(--frame);
    background: rgba(255, 255, 255, 0.6);
    text-align: center;
  }
  .serving {
    position: absolute;
    left: 0;
    right: 0;
    top: 118px;
    font-family: "Anton", sans-serif;
    font-size: 168px;
    line-height: 1;
    color: var(--ink-grey);
    letter-spacing: 52px;
    padding-left: 52px;
  }
  .area {
    position: absolute;
    left: 0;
    right: 0;
    top: 306px;
    font-family: "Montserrat", sans-serif;
    font-weight: 800;
    font-size: 34px;
    color: var(--ink-grey);
    letter-spacing: 3px;
  }
  .licensed {
    position: absolute;
    left: 0;
    right: 0;
    top: 462px;
    font-family: "Montserrat", sans-serif;
    font-weight: 800;
    font-size: 48px;
    line-height: 66px;
    color: var(--ink-grey);
    letter-spacing: 6px;
  }
  .license-number {
    position: absolute;
    left: 0;
    right: 0;
    top: 596px;
    font-family: "Anton", sans-serif;
    font-size: 104px;
    line-height: 1;
    color: var(--ink-navy);
    letter-spacing: 24px;
    padding-right: 80px;
  }
  .call-to-action {
    position: absolute;
    left: 0;
    right: 0;
    top: 846px;
    font-family: "Montserrat", sans-serif;
    font-weight: 800;
    font-size: 29px;
    color: var(--ink-navy);
    letter-spacing: 4px;
  }
  .website {
    position: absolute;
    left: 0;
    right: 0;
    top: 888px;
    font-family: "Roboto", sans-serif;
    font-weight: 400;
    font-size: 68px;
    line-height: 1;
    color: var(--ink-grey);
  }
  .phone {
    position: absolute;
    left: 640px;
    top: 2570px;
    width: 510px;
    text-align: right;
    font-family: "Anton", sans-serif;
    font-size: 72px;
    line-height: 1;
    color: var(--ink-navy);
    letter-spacing: 3px;
  }
</style>
</head>
<body>
<main class="rack-card">
  <div class="interior-photo" role="img" aria-label="Bright remodeled galley kitchen with white counters, grey cabinets and a patterned tile floor"></div>

  <svg class="wave-layer" viewBox="0 0 1200 2683" aria-hidden="true">
    <path class="top-orange" fill="var(--orange)" d="M0 0 H1200 Q1000 110 700 200 Q250 330 0 530 Z"/>
    <path class="top-navy" fill="var(--navy)" d="M0 530 Q250 330 700 200 Q1000 110 1200 0 V590 Q900 520 500 540 Q200 555 0 530 Z"/>
    <path class="bottom-orange-left" fill="var(--orange)" d="M0 2010 Q500 2050 1000 2330 L1200 2420 V2683 H0 Z"/>
    <path class="bottom-orange-right" fill="var(--orange-deep)" d="M450 2683 Q800 2400 1200 2110 V2683 Z"/>
    <path class="bottom-navy" fill="var(--navy)" d="M0 2480 Q400 2560 760 2683 H0 Z"/>
  </svg>

  <header class="brand">
    <div class="brand-mark"></div>
    <div class="brand-name">K TANDEM</div>
    <div class="brand-sub">BUILDERS</div>
  </header>

  <section class="info-panel">
    <div class="serving">SERVING</div>
    <div class="area">MARION COUNTY AND THE HERONFIELD</div>
    <div class="licensed">WE ARE A LICENSED AND<br>INSURED CONTRACTOR</div>
    <div class="license-number">CRC4871093</div>
    <div class="call-to-action">SEND US YOUR INSPECTION SUMMARY TODAY</div>
    <div class="website">www.BrindleyRenovator.com</div>
  </section>

  <div class="phone">555-318-4762</div>
</main>
</body>
</html>
```